Web Design for Tolvek Education Group
Tolvek Education Group
Web Design for Tolvek Education Group - Education
Creative Brief
Education
Tolvekeducationgroup.com
Company seeks to provide education products in Higher Education in emerging markets.
Elegant
Refer to Logo
left side
http://www.marplestoninc.example/
http://www.qrbt.example/
http://www.wendorleducation.example/
http://www.pvu.example/ Use less red in the overall web design but feel free to add a third color that would compliment colors in the logo.

```html
<!DOCTYPE html>
<html lang="en">
<head>
<meta charset="utf-8">
<title>Tolvek Education Group</title>
<link rel="stylesheet" href="https://fonts.googleapis.com/css2?family=PT+Sans+Narrow:wght@400;700&family=Open+Sans:wght@400;600;700&display=swap">
<style>
:root{
  --red:#c4161c;
  --red-dark:#8e0d12;
  --ink:#2b2b2b;
  --text:#555;
  --grey:#8a8a8a;
  --page:#eeeeee;
  --panel:#ffffff;
  --bar:#1d1d1d;
  --line:#dcdcdc;
}
*{box-sizing:border-box;margin:0;padding:0}
html,body{width:1200px;height:1027px;overflow:hidden}
body{position:relative;background:var(--page);font-family:"Open Sans",Arial,sans-serif;color:var(--text)}
.abs{position:absolute}
.topbar{left:0;top:0;width:1200px;height:25px;background:linear-gradient(#3a3a3a,#111)}
.topbar .help{left:190px;top:4px;color:#fff;font:700 14px "Open Sans",Arial,sans-serif}
.topbar .login{left:952px;top:4px;color:#fff;font:700 14px "Open Sans",Arial,sans-serif}
.brand{left:205px;top:60px;display:flex;align-items:center;gap:14px}
.brand .mark{width:58px;height:58px;background:var(--red)}
.brand .name{font:700 26px/1 "PT Sans Narrow",Arial,sans-serif;color:var(--ink);text-transform:uppercase;letter-spacing:1px}
.nav{left:548px;top:120px;display:flex;gap:26px;align-items:center;font:400 15px "PT Sans Narrow",Arial,sans-serif;color:#555;text-transform:uppercase}
.nav .home{display:flex;align-items:center;gap:5px}
.member{left:181px;top:153px;width:841px;height:30px;background:linear-gradient(#e0262c,var(--red));color:#fff;text-align:center;font:700 18px/30px "PT Sans Narrow",Arial,sans-serif;letter-spacing:.5px}
.hero{left:181px;top:189px;width:841px;height:248px;box-shadow:0 1px 4px rgba(0,0,0,.25)}
.hero .photo{position:absolute;left:0;top:0;width:529px;height:248px;background:linear-gradient(135deg,#c9b59a,#8c6a4e 55%,#b8352c)}
.hero .copy{position:absolute;left:529px;top:0;width:312px;height:248px;background:linear-gradient(#d21c22,var(--red-dark));color:#fff;padding:24px 22px}
.hero h1{font:700 22px/1.1 "PT Sans Narrow",Arial,sans-serif;text-transform:uppercase;margin-bottom:8px}
.hero p{font-size:11.5px;line-height:18px}
.hero .more{position:absolute;right:12px;bottom:12px;background:#fff;color:var(--red);font:700 11px/18px "Open Sans",Arial,sans-serif;padding:0 12px;text-transform:uppercase}
.panel{background:var(--panel);box-shadow:0 1px 4px rgba(0,0,0,.18)}
.products{left:181px;top:447px;width:841px;height:231px;padding:18px 22px}
.products h2,.col h2{font:700 22px "PT Sans Narrow",Arial,sans-serif;color:var(--ink)}
.products h2{border-bottom:1px solid var(--line);padding-bottom:6px}
.product-list{display:flex;justify-content:space-around;margin-top:14px}
.product{width:170px;text-align:center}
.product .pic{width:110px;height:72px;margin:0 auto 14px;background:linear-gradient(#d6d6d6,#7d7d7d)}
.product p{font:400 14px/1.35 "PT Sans Narrow",Arial,sans-serif;color:#333}
.btn-dark{background:var(--red-dark);color:#fff;font:700 12px/22px "Open Sans",Arial,sans-serif;padding:0 12px}
.products .btn-dark{position:absolute;right:0;bottom:0}
.col{top:690px;height:195px;padding:14px 18px}
.help-col{left:181px;width:322px}
.news-col{left:516px;width:506px}
.col h2{border-bottom:1px solid var(--line);padding-bottom:4px;margin-bottom:10px}
.help-col h2{text-transform:uppercase}
.help-col p{font-size:11px;line-height:17px}
.readmore{position:absolute;left:18px;bottom:12px;color:var(--red);font-size:12px}
.news-list{list-style:none}
.news-list li{display:flex;gap:8px;font-size:10.5px;line-height:14px;margin-bottom:7px;color:#444;text-decoration:underline}
.news-list li::before{content:"";flex:0 0 5px;height:5px;margin-top:5px;background:var(--red)}
.news-col .btn-dark{position:absolute;right:0;bottom:0;background:var(--red)}
.newsletter{left:181px;top:897px;width:841px;height:36px;background:linear-gradient(#b81318,var(--red-dark));display:flex;align-items:center;padding-left:125px;gap:14px}
.newsletter .label{color:#fff;font:700 20px "PT Sans Narrow",Arial,sans-serif;margin-right:12px}
.newsletter .field{width:167px;height:22px;background:#fff;font-size:11px;line-height:22px;padding-left:8px;color:#999}
.newsletter .submit{width:92px;height:22px;background:#eee;font-size:11px;line-height:22px;text-align:center;color:#333}
.footer{left:0;top:933px;width:1200px;height:94px;background:var(--bar)}
.footer .links{position:absolute;left:430px;top:14px;display:flex;gap:18px;color:#ddd;font-size:12px}
.footer .copy{position:absolute;left:190px;top:66px;color:#aaa;font-size:10px}
.footer .follow{position:absolute;left:793px;top:58px;display:flex;align-items:center;gap:8px;color:#fff;font:700 15px "PT Sans Narrow",Arial,sans-serif}
.footer .follow span.sq{width:22px;height:22px;background:#666;display:inline-block}
</style>
</head>
<body>
<div class="abs topbar">
  <div class="abs help">Need help? Call us: 012 555 0148</div>
  <div class="abs login">Log in</div>
</div>

<div class="abs brand"><span class="mark"></span><span class="name">Tolvek<br>Education Group</span></div>

<nav class="abs nav">
  <span class="home"><svg width="14" height="13" viewBox="0 0 14 13"><path d="M7 0L0 6h2v7h4V9h2v4h4V6h2z" fill="#555"/></svg>Home</span>
  <span>Products</span><span>Solutions</span><span>Services</span><span>Partners</span><span>Contact Us</span>
</nav>

<div class="abs member">Become a member »</div>

<section class="abs hero">
  <div class="photo" role="img" aria-label="Classroom photo of students raising hands in front of a teacher"></div>
  <div class="copy">
    <h1>Technology for higher education</h1>
    <p>Lorem ipsum dolor sit amet, consectetur adipiscing elit. Nam cursus. Morbi ut mi. Nullam enim leo, egestas id, condimentum at, laoreet mattis, massa. Sed eleifend nonummy diam. Praesent mauris ante, elementum et, bibendum at, posuere sit amet, nibh. Duis tincidunt lectus quis dui viverra vestibulum.</p>
    <span class="more">Read more</span>
  </div>
</section>

<section class="abs panel products">
  <h2>Products for higher education</h2>
  <div class="product-list">
    <div class="product"><div class="pic" role="img" aria-label="Interactive whiteboard product"></div><p>Tavro Board interactive<br>whiteboards</p></div>
    <div class="product"><div class="pic" role="img" aria-label="Interactive pen display product"></div><p>Tavro Lectern 40 line<br>interactive pen display</p></div>
    <div class="product"><div class="pic" role="img" aria-label="Document camera product"></div><p>Tavro Document Camera</p></div>
    <div class="product"><div class="pic" role="img" aria-label="Math software box"></div><p>Tavro Lesson Math Kit</p></div>
  </div>
  <span class="btn-dark">read more »</span>
</section>

<section class="abs panel col help-col">
  <h2>Help you to get success</h2>
  <p>Lorem ipsum dolor sit amet, consectetur adipiscing elit. Nam cursus. Morbi ut mi. Nullam enim leo, egestas id, condimentum at, laoreet mattis, massa. Sed eleifend nonummy diam. Praesent mauris ante, elementum et, bibendum at, posuere sit amet, nibh. Duis tincidunt lectus quis dui viverra vestibulum.</p>
  <span class="readmore">Read more</span>
</section>

<section class="abs panel col news-col">
  <h2>Latest News</h2>
  <ul class="news-list">
    <li>Lorem ipsum dolor sit amet, consectetur adipiscing elit. Nam cursus. Morbi ut mi. Nullam enim leo, egestas id, condimentum at.</li>
    <li>Lorem ipsum dolor sit amet, consectetur adipiscing elit. Nam cursus. Morbi ut mi. Nullam enim leo, egestas id, condimentum at.</li>
    <li>Lorem ipsum dolor sit amet, consectetur adipiscing elit. Nam cursus. Morbi ut mi. Nullam enim leo, egestas id, condimentum at.</li>
  </ul>
  <span class="readmore">Read more</span>
  <span class="btn-dark">read more »</span>
</section>

<div class="abs newsletter">
  <span class="label">Newsletter</span>
  <span class="field">Name</span>
  <span class="field">E-mail address</span>
  <span class="submit">Subscribe</span>
</div>

<footer class="abs footer">
  <div class="links"><span>Home</span><span>Products</span><span>Solutions</span><span>Services</span><span>Partners</span><span>Contact Us</span></div>
  <div class="copy">Copyright 2013 Tolvek. All rights reserved.</div>
  <div class="follow">Follow us on <span class="sq"></span><span class="sq"></span><span class="sq"></span><span class="sq"></span></div>
</footer>
</body>
</html>
```